Smart Home App Needs 4 Mockup Screens. Extra Work Guaranteed for Winner

BACKGROUND
Our company, Lumora, is launching an exciting new app early next year. And we need some examples of what our app will look like to show to some of the biggest retailers in the world. We hope that this project will lead to regular work as we have a lot of new products planned for the app.

Our app will support baby, home and pet monitors (cameras) as well as the world's first smart pet flap.

The monitors allow you to do much more than just watch live video. By monitoring and providing information on sound, movement and temperature the app provides the user with instant peace of mind wherever they are. If anything has changed the user can be alerted via notifications. If motion is detected the user will receive a clip of the whole event moments after it has happened.

The Smart Pet Flap is packed full of features too. From letting you decide when your pet can or can't go outside from your mobile, to automatically opening if a fire is detected (along with a whole host of other features) - this really is the most advanced pet flap in the world.

REQUIREMENTS
We need 4 mock-up screens creating to show the UI of our app.
1. Camera Home Page
2. Camera Notifications Page
3. Pet Flap Fire Alarm Warning Page
4. Extreme Weather Warning Page

Optional - Happy to Pay the Winner Extra for these Designs
5. Start Up/Log In Page
6. Pet Flap Notification Example
7. Pet Flap Scheduler Page (your choice)
(SEE LUMORA APP DESIGN COMPETITION - ATTACHED)

STYLE GUIDE
As you'll see from our wireframes we want our app to be very minimal and modern. The predominant colour will be white but where colour is used it should be bright (see our colour palette - which we will provide shortly).

INSPIRATION
We love the UI of Finchly (home surveillance). Also check out Vesk (smart thermostat).
(SEE LUMORA UI EXAMPLES ATTACHED)

LOGO
We love our logo. Feel free to use it in creative ways.

So far we're also using it as a kind of beacon to indicate if everything is ok.

LOGO COLOURS & APP COLOURS
As mentioned, we are thinking of using the green logo to indicate that everything is ok (and also for the pet app in general). We reserve red for when something has happened (normally bad) and needs attention, like a fire alarm going off.

The app will be predominantly black and white with the odd minimal flash of colour (probably primary colour)
We'll upload a colour scheme as soon as we have it.

CONTACT
Please message us for more details - we'll do our best to reply promptly.

FUTURE WORK
We will need extra screens made straight after the competition is over and there should be additional regular work after this.

Target Market(s)

Our app will be used by young professionals, to young parents to grandparents. The design must be contemporary but timeless and easy to use no matter how good you are with technology.

Industry/Entity Type

Pet

Font styles to use
Sans Serif

Colors
faee3f
33a6d7
ec1f27
acd036
32b7a4

Requirements
Must have
• Beautiful, minimal design. Make sure you spend time looking at the Finchly and Vesk apps before starting.

For the videos make sure you use sensible images - that you'd expect to see from a monitor (high resolution images if possible)
Nice to have
• Creative use of our logo.
Should not have
• Too much detail/clutter/colours. Ugly fonts.

```html
<!DOCTYPE html>
<html lang="en">
<head>
<meta charset="utf-8">
<title>Lumora – Camera Home</title>
<link rel="stylesheet" href="https://fonts.googleapis.com/css2?family=Montserrat:wght@300;400;500;700;800&display=swap">
<style>
  :root {
    --stage: #e6e6e6;
    --white: #ffffff;
    --ink: #3a3a3a;
    --muted: #8a8a8a;
    --red: #ec1f27;
    --red-soft: #ef4a45;
    --orange: #f39a2b;
    --green: #acd036;
    --blue: #33a6d7;
    --shade: rgba(0,0,0,0.35);
  }
  * { box-sizing: border-box; margin: 0; padding: 0; }
  html, body { width: 1200px; height: 840px; overflow: hidden; }
  body {
    background: var(--stage);
    font-family: "Montserrat", sans-serif;
    color: var(--ink);
    position: relative;
  }
  .app-screen {
    position: absolute;
    left: 380px; top: 30px;
    width: 440px; height: 780px;
    background: var(--white);
    overflow: hidden;
    box-shadow: 0 10px 40px rgba(0,0,0,0.12);
    display: flex; flex-direction: column;
  }
  .app-header {
    height: 88px;
    background: linear-gradient(100deg, var(--red) 0%, var(--red) 55%, var(--red-soft) 100%);
    color: var(--white);
    position: relative;
  }
  .status-bar {
    height: 28px;
    display: flex; align-items: center; justify-content: space-between;
    padding: 0 10px;
    font-size: 13px; font-weight: 400;
  }
  .status-bar .carrier, .status-bar .power { display: flex; align-items: center; gap: 5px; }
  .signal { display: flex; gap: 2px; }
  .signal i { width: 7px; height: 7px; border-radius: 50%; border: 1px solid var(--white); display: block; }
  .signal i.on { background: var(--white); }
  .battery { width: 26px; height: 11px; border: 1px solid var(--white); border-radius: 2px; padding: 1px; }
  .battery span { display: block; width: 100%; height: 100%; background: var(--white); }
  .brand {
    position: absolute; left: 0; right: 0; top: 40px;
    display: flex; align-items: center; justify-content: center; gap: 8px;
    font-size: 20px; font-weight: 700; letter-spacing: 2px;
  }
  .brand-dot { width: 12px; height: 12px; border-radius: 50%; background: var(--white); }
  .tabs {
    height: 55px;
    display: flex; align-items: stretch;
    position: relative;
  }
  .menu-toggle {
    position: absolute; left: 14px; top: 19px;
    width: 24px; display: flex; flex-direction: column; gap: 5px;
  }
  .menu-toggle span { height: 2px; background: var(--red); display: block; }
  .tab {
    flex: 1; display: flex; align-items: center; justify-content: center;
    font-size: 17px; font-weight: 300; letter-spacing: 4px; color: var(--muted);
  }
  .tab.is-active { color: var(--ink); font-weight: 400; border-bottom: 3px solid var(--red); margin-left: 44px; }
  .live-feed {
    height: 210px; position: relative;
    background: linear-gradient(160deg, #6f625a 0%, #9a8577 35%, #b89470 55%, #7b6a5f 100%);
  }
  .live-feed::after { content: ""; position: absolute; inset: 0; background: linear-gradient(180deg, transparent 45%, var(--shade)); }
  .feed-caption { position: absolute; right: 18px; bottom: 30px; text-align: right; z-index: 1; }
  .feed-time { font-size: 46px; font-weight: 700; line-height: 1; }
  .feed-time .clock { color: var(--red); }
  .feed-time .day { color: var(--white); font-weight: 800; }
  .feed-name { margin-top: 6px; font-size: 13px; color: var(--white); letter-spacing: 1px; display: flex; justify-content: flex-end; align-items: center; gap: 8px; }
  .feed-status { position: absolute; left: 16px; bottom: 12px; z-index: 1; }
  .meter { height: 4px; display: flex; }
  .meter span { flex: 1; }
  .controls {
    height: 60px; display: flex; align-items: center; justify-content: space-around;
    padding: 0 10px;
  }
  .controls svg { width: 30px; height: 30px; }
  .camera-list { flex: 1; display: flex; flex-direction: column; }
  .camera-row {
    flex: 1; position: relative; border-top: 2px solid var(--white);
    display: flex; align-items: center; justify-content: flex-end; padding-right: 18px;
  }
  .camera-row::after { content: ""; position: absolute; inset: 0; background: rgba(0,0,0,0.25); }
  .camera-row.garden { background: linear-gradient(120deg, #4a4a3c, #7a7663 50%, #3f3b33); }
  .camera-row.hallway { background: linear-gradient(120deg, #a89478, #d8c6a8 50%, #8c7660); }
  .camera-row.nursery { background: linear-gradient(120deg, #5c6f73, #8fb0b0 50%, #6a7b80); }
  .camera-title { position: relative; z-index: 1; color: var(--white); font-size: 17px; font-weight: 700; letter-spacing: 2px; }
  .camera-title small { font-size: 15px; font-weight: 400; }
  .status-dot { position: absolute; left: 16px; bottom: 12px; width: 20px; height: 20px; border-radius: 50%; z-index: 1; }
  .status-dot.ok { background: var(--green); }
  .status-dot.alert { background: var(--red); }
</style>
</head>
<body>
  <main class="app-screen">
    <header class="app-header">
      <div class="status-bar">
        <div class="carrier">
          <div class="signal"><i class="on"></i><i class="on"></i><i class="on"></i><i></i><i></i></div>
          <span>NOVA</span>
          <svg width="14" height="10" viewBox="0 0 14 10" fill="none" stroke="#fff" stroke-width="1.5"><path d="M1 3.5a9 9 0 0 1 12 0M3.5 6a5.5 5.5 0 0 1 7 0"/><circle cx="7" cy="8.5" r="1" fill="#fff"/></svg>
        </div>
        <span class="clock-now">4:21 PM</span>
        <div class="power">
          <svg width="8" height="12" viewBox="0 0 8 12" fill="none" stroke="#fff" stroke-width="1.2"><path d="M1 3l6 6-3 2V1l3 2-6 6"/></svg>
          <span>100%</span>
          <div class="battery"><span></span></div>
        </div>
      </div>
      <div class="brand"><span class="brand-dot"></span>Lumora</div>
    </header>

    <nav class="tabs">
      <div class="menu-toggle"><span></span><span></span><span></span></div>
      <div class="tab is-active">Now</div>
      <div class="tab">Earlier</div>
    </nav>

    <section class="live-feed" role="img" aria-label="Live pet camera view: a boxer dog resting on a living room sofa">
      <div class="feed-caption">
        <div class="feed-time"><span class="clock">13:25</span> <span class="day">MONDAY</span></div>
        <div class="feed-name">
          <svg width="18" height="11" viewBox="0 0 18 11" fill="#fff"><path d="M0 0l7 5.5L0 11z"/><rect x="8" y="1" width="10" height="9" rx="1"/></svg>
          Pet Cam (Living Room)
        </div>
      </div>
      <span class="feed-status status-dot ok"></span>
    </section>

    <div class="meter"><span style="background:var(--red)"></span><span style="background:var(--orange)"></span><span style="background:var(--green)"></span><span style="background:var(--blue)"></span></div>

    <div class="controls">
      <svg viewBox="0 0 30 30" aria-label="Microphone"><rect x="10" y="3" width="10" height="16" rx="5" fill="var(--red)"/><path d="M6 14a9 9 0 0 0 18 0M15 23v4M9 27h12" fill="none" stroke="var(--red)" stroke-width="2.2"/></svg>
      <svg viewBox="0 0 30 30" aria-label="Temperature"><path d="M12 4a3 3 0 0 1 6 0v13a6 6 0 1 1-6 0z" fill="none" stroke="var(--orange)" stroke-width="2"/><circle cx="15" cy="22" r="3.5" fill="var(--orange)"/><path d="M15 10v12" stroke="var(--orange)" stroke-width="2"/></svg>
      <svg viewBox="0 0 30 30" aria-label="Storage"><g fill="var(--green)"><ellipse cx="15" cy="23" rx="11" ry="4.5"/><ellipse cx="15" cy="16" rx="11" ry="4.5"/><ellipse cx="15" cy="9" rx="11" ry="4.5"/></g><g fill="none" stroke="#fff" stroke-width="1"><path d="M4 9a11 4.5 0 0 0 22 0M4 16a11 4.5 0 0 0 22 0"/></g></svg>
      <svg viewBox="0 0 30 30" aria-label="Expand"><g fill="none" stroke="var(--blue)" stroke-width="2.4" stroke-linecap="round"><path d="M11 11L3 3M3 9V3h6M19 11l8-8M21 3h6v6M11 19l-8 8M3 21v6h6M19 19l8 8M27 21v6h-6"/></g></svg>
    </div>

    <section class="camera-list">
      <div class="camera-row garden" role="img" aria-label="Garden camera view of a backyard with a wooden fence">
        <span class="camera-title">THE GARDEN <small>(BACKYARD)</small></span>
        <span class="status-dot ok"></span>
      </div>
      <div class="camera-row hallway" role="img" aria-label="Front door camera view of a hallway">
        <span class="camera-title">THE FRONT DOOR <small>(HALLWAY)</small></span>
        <span class="status-dot ok"></span>
      </div>
      <div class="camera-row nursery" role="img" aria-label="Baby camera view of a nursery with a cot">
        <span class="camera-title">BABY CAM <small>(NURSERY)</small></span>
        <span class="status-dot alert"></span>
      </div>
    </section>
  </main>
</body>
</html>
```